Grand Bridal Pastry Selling Method needs finishing touches to website.

We have a temporary website located at http://www.brivantaworks.example/qk/.
We are doing a responsive design and have created the architecture (layout). However, we need a professional makeover for the graphic elements and colors of the website. The website will be selling a sales course to mostly women who sell wedding cakes.
The photos within the posted website are for illustrative purposes. We will use our own photos after the website is redone.
We are open to changing the font styles, borders, header, and anything else as long as the layout is not changed.
Target Market(s)
75% women age 25-50 and men 30-60.
Industry/Entity Type
Architecture
Colors
Designer to choose colors to be used in the design.
Look and feel
Each slider illustrates characteristics of the customer's brand and the style your logo design should communicate.

```html
<!DOCTYPE html>
<html lang="en">
<head>
<meta charset="utf-8">
<title>Brivanta Works – Wedding Cake Sales</title>
<link href="https://fonts.googleapis.com/css2?family=Open+Sans:wght@300;400;600&family=Ubuntu:wght@400;500&display=swap" rel="stylesheet">
<style>
:root{
  --brand:#cc4f7d;
  --brand-dark:#b03a66;
  --accent-red:#a8131b;
  --ink:#555;
  --ink-soft:#777;
  --hero-bg:#ececec;
  --panel:#3d3d3d;
  --footer:#2d2d2d;
  --footer-line:#444;
  --white:#fff;
}
*{box-sizing:border-box;margin:0;padding:0}
html,body{width:1078px;height:1200px;overflow:hidden}
body{position:relative;font-family:"Open Sans",Arial,sans-serif;color:var(--ink);background:var(--white)}
.abs{position:absolute}

.site-header{left:0;top:0;width:1078px;height:67px;background:var(--brand)}
.brand-name{left:89px;top:9px;font-family:"Ubuntu",sans-serif;font-size:37px;color:var(--white);font-weight:400;letter-spacing:-.2px}
.main-nav{right:95px;top:25px;display:flex;gap:25px;font-size:13px;font-weight:600;color:var(--white)}

.hero{left:0;top:67px;width:1078px;height:486px;background:linear-gradient(90deg,#e9e9e9 0%,#f4f4f4 55%,#f7f4f5 100%)}
.hero-photo{left:740px;top:67px;width:338px;height:486px;background:radial-gradient(ellipse at 45% 45%,#fbf7f8 0%,#f4e3e8 55%,#efeff0 100%)}
.headline{left:89px;top:98px;font-weight:300;font-size:36px;line-height:44px;color:#6b6b6b}
.headline em{font-style:normal;color:var(--accent-red)}

.video-frame{left:92px;top:215px;width:509px;height:308px;background:var(--white);box-shadow:0 1px 4px rgba(0,0,0,.35);padding:5px}
.video-still{width:100%;height:100%;background:linear-gradient(135deg,#5a4a3a 0%,#3b3025 50%,#231c16 100%);position:relative}
.play-btn{position:absolute;left:238px;top:122px;width:52px;height:52px;border-radius:7px;background:rgba(30,30,30,.75)}
.play-btn svg{position:absolute;left:16px;top:15px}

.optin{left:602px;top:300px;width:291px;height:217px;background:rgba(55,55,55,.92);border-radius:0 0 3px 3px;padding:14px 19px 0}
.optin-title{text-align:center;color:var(--white);font-size:15px;line-height:24px;font-weight:400}
.optin-title span{display:block;font-size:20px;line-height:26px}
.field{margin-top:10px;height:31px;background:var(--white);border-radius:2px;padding:0 13px;font-size:13px;line-height:31px;color:#666}
.field + .field{margin-top:8px}
.optin-foot{display:flex;justify-content:space-between;align-items:center;margin-top:10px}
.optin-foot small{font-size:10px;color:#ddd}
.cta{background:#f6a9c0;color:#7a1a3c;font-size:13px;font-weight:600;padding:6px 11px;border-radius:2px}

.section-title{left:0;top:583px;width:1078px;text-align:center;color:var(--brand);font-size:21px;font-weight:400}

.card{top:637px;width:297px}
.card-media{height:157px}
.card p{margin-top:10px;text-align:center;font-size:14px;line-height:21px;padding:0 14px;color:var(--ink)}
.card.is-active p{color:var(--brand)}
.btn{display:block;width:max-content;margin:14px auto 0;border:1px solid #ccc;border-radius:2px;padding:4px 11px;font-size:13px;color:var(--ink);background:var(--white)}
.card.is-active .btn{background:linear-gradient(#d9587f,var(--brand-dark));color:var(--white);border-color:var(--brand-dark)}

.divider{left:89px;top:940px;width:899px;height:1px;background:#e2e2e2}
.seen-label{left:0;top:958px;width:1078px;text-align:center;font-size:14px;color:var(--ink)}
.press{left:95px;top:1003px;width:880px;display:flex;justify-content:space-between;align-items:center;font-size:15px;font-weight:600;color:#9a9a9a}

.site-footer{left:0;top:1069px;width:1078px;height:131px;background:var(--footer)}
.footer-nav{left:0;top:1092px;width:1078px;display:flex;justify-content:center;gap:56px;font-size:13px;color:#bbb}
.footer-nav span::before{content:"• ";font-size:9px;color:#888}
.footer-line{left:89px;top:1132px;width:899px;height:1px;background:var(--footer-line)}
.copyright{left:91px;top:1155px;font-size:13px;color:#bbb}
.social{right:88px;top:1152px;display:flex;gap:8px;font-size:12px;color:#bbb}
</style>
</head>
<body>
<header class="abs site-header"></header>
<div class="abs brand-name">Brivanta Works</div>
<nav class="abs main-nav"><span>Who Is Lev Marsh</span><span>Why Lev Is Sharing His Secrets</span><span>Contact</span></nav>

<section class="abs hero"></section>
<div class="abs hero-photo" role="img" aria-label="Tiered white wedding cake with pink sugar roses and champagne glasses"></div>
<h1 class="abs headline">Cracking The <em>“Secret Code”</em><br>That Unlocks Your Wedding Cake Sales!</h1>

<div class="abs video-frame">
  <div class="video-still" role="img" aria-label="Video still of a photo booth showroom with price text">
    <div class="play-btn"><svg width="22" height="22" viewBox="0 0 22 22"><path d="M3 1 L20 11 L3 21 Z" fill="#fff"/></svg></div>
  </div>
</div>

<form class="abs optin">
  <p class="optin-title">FREE Videos To Help You Sell More Wedding Cakes At Higher Prices…<span>Immediately</span></p>
  <div class="field">Name</div>
  <div class="field">E-mail</div>
  <div class="optin-foot"><small>No Spam. I Promise.</small><span class="cta">Get Instant Access</span></div>
</form>

<h2 class="abs section-title">3 Leading-Edge Techniques for Convincing Brides to Choose You</h2>

<article class="abs card is-active" style="left:90px">
  <div class="card-media" role="img" aria-label="Artists painting a colourful two-sided face design" style="background:linear-gradient(90deg,#e0a63a,#3aa9a4 50%,#e8a53d)"></div>
  <p>In the first video, discover a sales growth secret that reveals the "Two Faces Of Your Wedding Cake Business."</p>
  <span class="btn">Read more</span>
</article>
<article class="abs card" style="left:390px">
  <div class="card-media" role="img" aria-label="Uncertain woman shrugging on a white background" style="background:linear-gradient(#f4f4f4,#e6e6e6)"></div>
  <p>In the second video you'll peek at my most effective psychological sales secret called "The Insecurity Gap."</p>
  <span class="btn">Read more</span>
</article>
<article class="abs card" style="left:690px">
  <div class="card-media" role="img" aria-label="Glowing blue world map on black" style="background:radial-gradient(ellipse at 50% 40%,#3a7fd0 0%,#0f2f66 55%,#03081a 100%)"></div>
  <p>In the third video, you will find out how to use Your "External Perception to WIN more wedding cake orders.</p>
  <span class="btn">Read more</span>
</article>

<div class="abs divider"></div>
<p class="abs seen-label">Lev Marsh as seen</p>
<div class="abs press">
  <span>Harbor Daily</span><span>The Lantern</span><span>Ridge TV</span><span>Market Ledger</span><span>Keystone</span><span>Bayside Courier</span><span>Venture</span><span>Metro 24</span>
</div>

<footer class="abs site-footer"></footer>
<nav class="abs footer-nav"><span>Home</span><span>Who Is Lev Marsh</span><span>Why Lev Is Sharing His Secrets</span><span>Contact</span></nav>
<div class="abs footer-line"></div>
<p class="abs copyright">Copyright © 2014 Brivanta Works. All rights reserved.</p>
<div class="abs social"><span>Sharebook</span><span>Chirper</span></div>
</body>
</html>
```